TARPLOAD business card design

TARPLOAD is a manufacturer of skip bags supplying both the domestic and commercial market. We wish to convey core characteristics of strength, professionalism and reliability to our customers. We are after a business card that uses our company colours of black and yellow as well as incorporating our logo. Our customers are predominantly in the construction or hardware industry. It is important the cards are professional as we are a small company wishing to appear larger than we actually are. more info on the company and product available at www.tarpload-example.com.au

Target Market(s)

hardware buyers, contruction company owners

Industry/Entity Type

Construction

Requirements
Must have
• company colours of black and yellow - No other colours or variation of yellow black. our company logo. card design must convey "tough"
• Card design must be landscape
• Details to be included on the card are:
• Name and Tiltle
• Phone number : 1300 41 62 53
• Mobile: 0452 718 903
• Fax: 03 9617 4852
• email: dale.hendry@tarpload-example.com.au
• address: PO Box 517, Kelvindale, VIC,3294
• Text in white when on a black background
Nice to have
• I like the idea of the back of the card being black with lighter circle area in the middle with black logo in the centre. Similar to the attached "iconic" card

```html
<!DOCTYPE html>
<html lang="en">
<head>
<meta charset="utf-8">
<title>TARPLOAD business card</title>
<link href="https://fonts.googleapis.com/css2?family=Mulish:ital,wght@0,400;0,700;0,800;0,900;1,400&display=swap" rel="stylesheet">
<style>
  :root {
    --black: #000000;
    --ink: #111111;
    --yellow: #f2dc1a;
    --white: #ffffff;
    --glow-core: #b5b5b5;
    --glow-mid: #555555;
  }
  * { margin: 0; padding: 0; box-sizing: border-box; }
  html, body { width: 1200px; height: 1200px; overflow: hidden; background: var(--white); }
  body { position: relative; font-family: "Mulish", Arial, sans-serif; color: var(--ink); }

  .card { position: absolute; left: 161px; width: 857px; height: 528px; }

  .card-back {
    top: 53px;
    background: var(--black);
    overflow: hidden;
  }
  .card-back .glow {
    position: absolute; inset: 0;
    background: radial-gradient(ellipse 360px 250px at 50% 62%, var(--glow-core) 0%, var(--glow-mid) 50%, var(--black) 92%);
  }
  .card-back .wordmark {
    position: absolute; left: 0; right: 0; top: 392px;
    text-align: center;
    font-weight: 900; font-size: 90px; letter-spacing: 4px;
    color: var(--black);
    line-height: 1;
  }

  .card-front {
    top: 614px;
    background: var(--white);
    border-top: 14px solid var(--yellow);
    border-bottom: 14px solid var(--yellow);
    box-shadow: 0 0 0 1px #e6e6e6;
  }
  .holder { position: absolute; right: 58px; top: 106px; text-align: right; }
  .holder-name { font-weight: 800; font-size: 36px; line-height: 1.1; }
  .holder-title { font-style: italic; font-size: 23px; margin-top: 4px; }

  .front-wordmark {
    position: absolute; left: 40px; top: 418px;
    font-weight: 900; font-size: 34px; letter-spacing: 0.5px;
    color: var(--ink); line-height: 1;
    white-space: nowrap;
  }
  .divider {
    position: absolute; left: 278px; top: 284px;
    width: 3px; height: 186px; background: var(--ink);
  }
  .contact { position: absolute; left: 309px; top: 290px; list-style: none; }
  .contact li { font-size: 24px; line-height: 33.6px; white-space: nowrap; }
  .contact b { font-weight: 800; }
  .contact .web { font-weight: 800; }
</style>
</head>
<body>
  <section class="card card-back" aria-label="Card back">
    <div class="glow"></div>
    <div class="wordmark">TARPLOAD</div>
  </section>

  <section class="card card-front" aria-label="Card front">
    <div class="holder">
      <div class="holder-name">Dale Hendry</div>
      <div class="holder-title">Managing Director</div>
    </div>
    <div class="front-wordmark">TARPLOAD</div>
    <div class="divider"></div>
    <ul class="contact">
      <li>PO Box 517, Kelvindale, VIC, 3294</li>
      <li><b>E:</b> dale.hendry@tarpload-example.com.au</li>
      <li><b>M:</b> 0452 718 903</li>
      <li><b>P:</b> 1300 41 62 53</li>
      <li><b>F:</b> 03 9617 4852</li>
      <li class="web">www.tarpload-example.com.au</li>
    </ul>
  </section>
</body>
</html>
```